Lab & Medical Equipment Repair Company Business Card Design

Looking for business card design for a lab & medical equipment repair company. Must be double-sided and must list our primary pieces we repair. Optionally, can include a QR code which should direct to our website.

Clients are usually doctors, so the card must be designed with a professional tone; however, we are looking for creativity in presentation. Open as to what should be on the front and back on card.

** Looking for a CLEAN design with creativity. Please use "Nice to have Priorities" items with discretion.

Core marketing logic:

When lab or medical equipment needs repair, most doctors call the manufacturers and schedule a technician to repair. Usually this takes one or two weeks, and, often, their work spoils. Alternatively, the doctors could hold equipment insurance which gives them a less expensive cost, but the response time is still similarly long.

Our company provides both competitive rates and one of the fastest response times in the industry. Technicians are dispatched directly to the site of the equipment, usually within 24 hours. Equipment under contract receives the same fast response time and includes complimentary annual maintenance. We service some of the most prestigious facilities in the Pittsburgh area and cover all of Western Pennsylvania, Ohio, and West Virginia.

Target Market(s)

Laboratory owners (doctors)

Industry/Entity Type

Marketing

Requirements
Must have
• Company Logo
Employee Name: Ray Dunwoody
Employee Title: CEO
Company Phone: 724-555-0187
Company Fax: 866-555-0143
Company Address: PO Box 518 Harmony Glen, PA 16099
Company Website: www.brightfixlabtech.example
Equipment We Service: Freezers, Cryostorage, Incubators, Centrifuges, Refrigerators, Environmental Chambers, Autoclaves, and more.

Nice to have
• Company Facebook: facebook.com/bfltllc
Company Twitter: @BFLTLLC
QR Code (link to website): www.brightfixlabtech.example

```html
<!DOCTYPE html>
<html lang="en">
<head>
<meta charset="utf-8">
<title>BrightFix Lab Tech – Business Card</title>
<link rel="stylesheet" href="https://fonts.googleapis.com/css2?family=Arimo:wght@700&family=Cormorant+Garamond:ital,wght@1,500&display=swap">
<style>
  :root {
    --page: #ffffff;
    --ink: #ffffff;
    --ink-soft: rgba(255,255,255,0.88);
    --night: #05040a;
    --violet: #2b2456;
    --plum: #3a1530;
    --teal: #0f2a33;
    --card-shadow: rgba(0,0,0,0.35);
  }
  * { box-sizing: border-box; margin: 0; padding: 0; }
  html, body {
    width: 1200px; height: 800px; overflow: hidden;
    background: var(--page);
  }
  .sheet {
    position: relative; width: 1200px; height: 800px;
    display: flex; align-items: center; justify-content: center; gap: 40px;
  }
  .card {
    position: relative; width: 540px; height: 310px; overflow: hidden;
    color: var(--ink);
    font-family: "Arimo", Arial, sans-serif; font-weight: 700;
    background:
      radial-gradient(ellipse 60% 45% at 15% 10%, var(--violet) 0%, transparent 70%),
      radial-gradient(ellipse 55% 50% at 85% 95%, var(--plum) 0%, transparent 75%),
      radial-gradient(ellipse 45% 40% at 20% 85%, var(--teal) 0%, transparent 70%),
      linear-gradient(150deg, #0b0a1c 0%, var(--night) 45%, #150913 100%);
    box-shadow: 0 10px 30px var(--card-shadow);
  }
  .brand { position: absolute; left: 30px; top: 26px; }
  .brand__mark {
    display: flex; align-items: center; gap: 8px;
    font-size: 40px; letter-spacing: 4px; line-height: 1;
  }
  .brand__dot {
    width: 12px; height: 12px; border-radius: 50%; background: var(--ink);
  }
  .brand__name { font-size: 15px; margin-top: 6px; }

  /* Front */
  .holder { position: absolute; left: 90px; right: 60px; top: 120px; }
  .holder__name {
    font-family: "Cormorant Garamond", Georgia, serif; font-style: italic; font-weight: 500;
    font-size: 56px; line-height: 1; text-align: center;
  }
  .rule-double {
    height: 5px; border-top: 1.5px solid var(--ink); border-bottom: 1px solid var(--ink);
  }
  .holder .rule-double { margin-top: 6px; }
  .holder__title { text-align: right; font-size: 14px; margin-top: 6px; }
  .front__web {
    position: absolute; bottom: 22px; left: 0; right: 0; text-align: center; font-size: 15px;
  }

  /* Back */
  .contact {
    position: absolute; left: 30px; bottom: 22px; list-style: none;
    font-size: 13.5px; line-height: 19px;
  }
  .contact li { display: flex; align-items: center; gap: 9px; white-space: nowrap; }
  .contact svg { width: 14px; height: 14px; flex: none; }
  .services { position: absolute; right: 26px; top: 72px; width: 190px; }
  .services__title { font-size: 14px; padding-bottom: 4px; }
  .services__list {
    margin-top: 20px; padding-left: 12px; font-size: 13px; line-height: 17px;
    list-style: none; color: var(--ink-soft);
  }
</style>
</head>
<body>
<main class="sheet">

  <section class="card card--front" aria-label="Card front">
    <div class="brand">
      <div class="brand__mark"><span>BFLT</span><span class="brand__dot"></span></div>
      <div class="brand__name">BrightFix Lab Tech</div>
    </div>
    <div class="holder">
      <h1 class="holder__name">Ray Dunwoody</h1>
      <div class="rule-double"></div>
      <p class="holder__title">CEO</p>
    </div>
    <p class="front__web">www.brightfixlabtech.example</p>
  </section>

  <section class="card card--back" aria-label="Card back">
    <div class="brand">
      <div class="brand__mark"><span>BFLT</span><span class="brand__dot"></span></div>
      <div class="brand__name">BrightFix Lab Tech</div>
    </div>

    <ul class="contact">
      <li>
        <svg viewBox="0 0 14 14" aria-hidden="true"><path d="M2 4 Q7 0 12 4 L10 6 L8.5 4.5 H5.5 L4 6 Z M3 7 H11 V12 H3 Z" fill="none" stroke="#fff" stroke-width="1.1"/></svg>
        <span>724-555-0187</span>
      </li>
      <li>
        <svg viewBox="0 0 14 14" aria-hidden="true"><rect x="1.5" y="4" width="11" height="8.5" fill="none" stroke="#fff" stroke-width="1.1"/><rect x="4" y="1.5" width="6" height="3" fill="none" stroke="#fff" stroke-width="1"/><path d="M4 7h6M4 9.5h6" stroke="#fff" stroke-width="1"/></svg>
        <span>866-555-0143</span>
      </li>
      <li>
        <svg viewBox="0 0 14 14" aria-hidden="true"><rect x="1" y="1" width="12" height="12" fill="none" stroke="#fff" stroke-width="1.1"/><path d="M3 4.5 L7 8 L11 4.5 M3 10 L5.5 7.5 M11 10 L8.5 7.5" fill="none" stroke="#fff" stroke-width="1"/></svg>
        <span>PO Box 518 Harmony Glen, PA 16099</span>
      </li>
      <li>
        <svg viewBox="0 0 14 14" aria-hidden="true"><rect x="1" y="1" width="12" height="12" fill="none" stroke="#fff" stroke-width="1.1"/><circle cx="7" cy="7" r="3.2" fill="none" stroke="#fff" stroke-width="1"/><path d="M3.8 7h6.4M7 3.8v6.4" stroke="#fff" stroke-width="0.8"/></svg>
        <span>www.brightfixlabtech.example</span>
      </li>
      <li>
        <svg viewBox="0 0 14 14" aria-hidden="true"><rect x="1" y="1" width="12" height="12" fill="none" stroke="#fff" stroke-width="1.1"/></svg>
        <span>friendpage.example/bfltllc</span>
      </li>
      <li>
        <svg viewBox="0 0 14 14" aria-hidden="true"><rect x="1" y="1" width="12" height="12" fill="none" stroke="#fff" stroke-width="1.1"/></svg>
        <span>@BFLTLLC</span>
      </li>
    </ul>

    <div class="services">
      <h2 class="services__title">Equipment We Service:</h2>
      <div class="rule-double"></div>
      <ul class="services__list">
        <li>Freezers,</li>
        <li>Cryostorage,</li>
        <li>Incubators,</li>
        <li>Centrifuges,</li>
        <li>Refrigerators,</li>
        <li>Environmental</li>
        <li>Chambers,</li>
        <li>Autoclaves, and more.</li>
      </ul>
    </div>
  </section>

</main>
</body>
</html>
```